Web Design Project

I need a website for a motorcycle sales business I have started.
I specialise in sourcing and importing older Brenton Falcaros.
I sell them or restore them pending on their condition. I could have up to 5-15 bikes at any one time for sale. I also sell secondhand spare parts.
I want to be able to upload pics and text for each bike, so I guess I may need a page for each bike with up to 10 medium resolution pics per page and a text box for around 100-200 words as well.
Ideally have a look at the Brenton Falcaro website.
I would like my site to be sophisticated but simple, understated but tough.
My colors are black and orange.

Target Market(s)

mostly guys aged from early 30's to 60's

Industry/Entity Type

Business

Requirements
Nice to have
• Pics that fade on the home page?
darker background?

```html
<!DOCTYPE html>
<html lang="en">
<head>
<meta charset="utf-8">
<title>Brenton Falcaro Classics</title>
<link href="https://fonts.googleapis.com/css2?family=Quicksand:wght@400;500;600&family=Open+Sans:wght@400;600;700&display=swap" rel="stylesheet">
<style>
  :root {
    --page-bg: #141414;
    --nav-top: #3a3a3a;
    --nav-bottom: #1c1c1c;
    --nav-divider: #0e0e0e;
    --nav-text: #9a9a9a;
    --white: #ffffff;
    --soft-white: #e6e6e6;
    --muted: #8a8a8a;
    --dim-text: #3b3b3b;
    --rule: #2c2c2c;
    --box-bg: #1a1a1a;
    --box-border: #2e2e2e;
    --orange: #f0a830;
    --red-orange: #d8402a;
    --photo-dark: #0b0b0c;
    --photo-mid: #2a1618;
  }
  * { margin: 0; padding: 0; box-sizing: border-box; }
  html, body { width: 1110px; height: 1200px; overflow: hidden; }
  body {
    background: var(--page-bg);
    font-family: "Open Sans", Arial, sans-serif;
    color: var(--white);
    position: relative;
  }
  .abs { position: absolute; }

  /* Header */
  .brand { left: 150px; top: 25px; display: flex; align-items: center; gap: 10px; }
  .brand-dot { width: 24px; height: 24px; border-radius: 50%; background: var(--orange); }
  .brand-name { font-size: 19px; font-weight: 700; letter-spacing: 0.3px; color: var(--white); }
  .social-line { right: 165px; top: 37px; font-size: 11px; color: var(--muted); }
  .social-line b { color: var(--white); font-weight: 700; }

  /* Navigation */
  .main-nav {
    left: 150px; top: 72px; width: 795px; height: 30px;
    background: linear-gradient(var(--nav-top), var(--nav-bottom));
    display: flex;
  }
  .main-nav a {
    display: block; height: 30px; line-height: 31px;
    font-size: 12px; letter-spacing: 0.5px; text-decoration: none;
    color: var(--nav-text); text-align: center;
    border-right: 1px solid var(--nav-divider);
  }
  .main-nav a.current { color: var(--white); }

  /* Slider */
  .hero-photo {
    left: 189px; top: 105px; width: 705px; height: 473px;
    background: radial-gradient(ellipse at 50% 55%, var(--photo-mid) 0%, #141012 40%, var(--photo-dark) 80%);
  }
  .slide-arrow {
    width: 20px; height: 116px; background: #101010;
    border: 1px solid #3a3a3a; display: flex; align-items: center; justify-content: center;
  }
  .slide-arrow.prev { left: 163px; top: 267px; }
  .slide-arrow.next { left: 902px; top: 279px; }

  /* Columns */
  .col-title {
    font-family: "Quicksand", Arial, sans-serif; font-weight: 500;
    font-size: 21px; color: var(--soft-white); letter-spacing: 0.5px;
    padding-bottom: 10px; border-bottom: 1px solid var(--rule);
  }
  .welcome { left: 150px; top: 585px; width: 253px; }
  .welcome-photo { margin-top: 24px; width: 237px; height: 108px;
    background: linear-gradient(90deg, #2a2a2a, #6a6a6a 45%, #3c3c3c 80%, #222); }
  .welcome-lead { margin-top: 26px; font-size: 9.5px; line-height: 18px; color: var(--dim-text); text-transform: uppercase; letter-spacing: 0.3px; }
  .welcome-body { margin-top: 8px; font-size: 10.5px; line-height: 18px; color: var(--dim-text); }
  .read-more { display: inline-flex; align-items: center; gap: 6px; margin-top: 21px; font-size: 11px; font-weight: 700; color: var(--white); text-decoration: none; }

  .services { left: 418px; top: 585px; width: 254px; }
  .service-list { list-style: none; margin-top: 14px; }
  .service-list li {
    height: 25.6px; line-height: 25px; font-size: 10.5px; color: var(--dim-text);
    border-bottom: 1px solid var(--rule); padding-left: 31px; position: relative;
  }
  .service-list li::before {
    content: ""; position: absolute; left: 16px; top: 11px;
    width: 3px; height: 3px; background: #6a6a6a;
  }
  .service-list li:last-child { border-bottom: none; }

  .info-box { background: var(--box-bg); border: 1px solid var(--box-border); width: 251px; }
  .phone-box { left: 687px; top: 592px; height: 89px; padding: 20px 0 0 20px; }
  .phone-number { font-family: "Quicksand", Arial, sans-serif; font-size: 24px; font-weight: 500; color: var(--white); }
  .phone-number .plus { color: var(--orange); }
  .phone-number .area { color: var(--red-orange); }
  .phone-hours { margin-top: 4px; margin-right: 20px; text-align: right; font-size: 9.5px; color: var(--muted); }
  .examples-box { left: 687px; top: 698px; height: 90px; padding: 23px 0 0 20px; }
  .examples-title { font-family: "Quicksand", Arial, sans-serif; font-size: 24px; font-weight: 500; color: var(--white); }
  .examples-link { display: inline-flex; align-items: center; gap: 6px; margin-top: 2px; font-size: 10.5px; color: #aaaaaa; text-decoration: none; }

  /* Footer */
  .footer-rule { left: 150px; top: 1055px; width: 795px; height: 1px; background: var(--rule); }
  .footer-nav { top: 1093px; font-size: 11px; font-weight: 700; color: var(--white); text-decoration: none; }
  .footer-nav.current { text-decoration: underline; }
  .footer-legal { top: 1093px; font-size: 11px; color: var(--muted); }
</style>
</head>
<body>
  <header>
    <div class="abs brand">
      <span class="brand-dot"></span>
      <span class="brand-name">COMPANY LOGO</span>
    </div>
    <p class="abs social-line">Follow us on <b>Chatline</b>, <b>Friendbook</b> and <b>Shotboard</b></p>
  </header>

  <nav class="abs main-nav">
    <a class="current" style="width:67px">HOME</a>
    <a style="width:73px">ABOUT</a>
    <a style="width:87px">GALLERY</a>
    <a style="width:144px">MOTORCYCLES</a>
    <a style="width:96px">CONTACTS</a>
  </nav>

  <div class="abs hero-photo" role="img" aria-label="Photograph of a red and black motorcycle on a dark studio background"></div>
  <div class="abs slide-arrow prev">
    <svg width="6" height="9" viewBox="0 0 6 9"><path d="M5 0.5 L1 4.5 L5 8.5" fill="none" stroke="#9a9a9a" stroke-width="1"/></svg>
  </div>
  <div class="abs slide-arrow next">
    <svg width="6" height="9" viewBox="0 0 6 9"><path d="M1 0.5 L5 4.5 L1 8.5" fill="none" stroke="#9a9a9a" stroke-width="1"/></svg>
  </div>

  <section class="abs welcome">
    <h2 class="col-title">WELCOME!</h2>
    <div class="welcome-photo" role="img" aria-label="Black and white photograph of a group of riders standing by a wall"></div>
    <p class="welcome-lead">Founded on a love for old steel and chrome, we source and import classic machines from abroad</p>
    <p class="welcome-body">Every bike that arrives in our workshop is inspected from frame to fuel tank. Some are sold as they stand, ready for a new owner to ride away. Others are stripped down and restored with care, using sound secondhand parts where they fit best. Drop in, take a look around and ask about the stock we hold.</p>
    <a class="read-more">Read more
      <svg width="9" height="7" viewBox="0 0 9 7"><path d="M0 3.5 H8 M5 0.5 L8 3.5 L5 6.5" fill="none" stroke="#ffffff" stroke-width="1.1"/></svg>
    </a>
  </section>

  <section class="abs services">
    <h2 class="col-title">OUR SERVICES</h2>
    <ul class="service-list">
      <li>Sourcing of older classic bikes</li>
      <li>Import and shipping from overseas</li>
      <li>Full frame off restorations</li>
      <li>Engine rebuilds and tuning work</li>
      <li>Paint, chrome and polishing</li>
      <li>Secondhand spare parts for sale</li>
      <li>Wiring and electrical repairs</li>
      <li>Pre-purchase inspections</li>
      <li>Registration and paperwork help</li>
      <li>Seat and trim upholstery</li>
      <li>Wheel rebuilds and new tyres</li>
      <li>Storage for winter months</li>
    </ul>
  </section>

  <aside>
    <div class="abs info-box phone-box">
      <p class="phone-number"><span class="plus">+</span><span class="area">(123)</span> 456-70192</p>
      <p class="phone-hours">Monday - Saturday: 7:30 am - 6:00 pm</p>
    </div>
    <div class="abs info-box examples-box">
      <p class="examples-title">EXAMPLES</p>
      <a class="examples-link">View all works
        <svg width="9" height="7" viewBox="0 0 9 7"><path d="M0 3.5 H8 M5 0.5 L8 3.5 L5 6.5" fill="none" stroke="#aaaaaa" stroke-width="1.1"/></svg>
      </a>
    </div>
  </aside>

  <footer>
    <div class="abs footer-rule"></div>
    <a class="abs footer-nav current" style="left:150px">HOME</a>
    <a class="abs footer-nav" style="left:195px">ABOUT</a>
    <a class="abs footer-nav" style="left:245px">GALLERY</a>
    <a class="abs footer-nav" style="left:428px">CONTACTS</a>
    <span class="abs footer-legal" style="left:799px">© 2012</span>
    <span class="abs footer-legal" style="left:854px">PRIVACY POLICY</span>
  </footer>
</body>
</html>
```